TideWillowNook.com needs updated website design.

TideWillowNook.com offers individuals a quick, hassle-free way of selling their car, rv, or boat in the Sun City Center, FL area. We will come to the customer's place of choosing in order to give them an in-person offer for their car, rv, or boat. Looking for a website design that will allow users to input their vehicle details as well as their contact info in order to schedule a time and place for our staff to come make them an offer. Currently have an active site that can be referenced.

Target Market(s)

Older people who no longer need their cars.

Industry/Entity Type

Automotive

Coding

Coded - Design and coding required

Number of Pages Required

3 page

Font styles to use
Sans Serif

Colors
a1cd3a
33b8a4

Requirements
Must have
• Trustworthy theme, Emphasis on capturing contact info (contact form visible at all times). Standard privacy policy. Wordpress theme

```html
<!DOCTYPE html>
<html lang="en">
<head>
<meta charset="utf-8">
<title>TideWillowNook.com – Sell Your Car, Boat or RV</title>
<link href="https://fonts.googleapis.com/css2?family=Mulish:wght@400;600;700;800&display=swap" rel="stylesheet">
<style>
:root{
  --teal:#33b8a4;
  --green:#a1cd3a;
  --pale-green:#d8e8b4;
  --ink:#1f2328;
  --muted:#6b7075;
  --line:#e6e8ea;
  --soft:#f4f5f6;
  --spec:#eef6f4;
  --white:#ffffff;
}
*{box-sizing:border-box;margin:0;padding:0}
html,body{width:1200px;height:4383px;overflow:hidden}
body{position:relative;background:var(--white);font-family:"Mulish",sans-serif;color:var(--ink)}
.abs{position:absolute}
.shapes{position:absolute;left:0;top:0;width:1200px;height:4383px}
.brand{position:absolute;display:flex;align-items:center;gap:12px}
.brand-name{font-weight:800;font-size:21px;color:var(--ink);line-height:1}
.brand-dot{width:40px;height:40px;border-radius:50%;background:var(--teal)}
/* header */
.phone-box{left:507px;top:20px;width:36px;height:36px;border-radius:6px;background:#5fd0bf;display:flex;align-items:center;justify-content:center}
.phone-text{left:557px;top:29px;color:#fff;font-size:15px;font-weight:600}
.menu{left:882px;top:29px;color:#fff;font-size:14px;display:flex;gap:10px;align-items:center}
.login{left:987px;top:20px;width:112px;height:36px;border:1.5px solid #fff;border-radius:18px;color:#fff;font-size:14px;display:flex;align-items:center;justify-content:center;gap:7px}
.advertise{right:100px;top:118px;color:#fff;font-weight:800;font-size:17px;letter-spacing:.3px}
.step{position:absolute;top:164px;width:28px;height:28px;border-radius:50%;background:var(--green);color:#fff;font-size:13px;font-weight:800;display:flex;align-items:center;justify-content:center}
.step-cap{position:absolute;top:204px;color:#fff;font-size:11.5px;line-height:16px}
/* hero */
.hero-title{left:100px;top:143px;font-size:37px;font-weight:700;line-height:38px;width:400px}
.hero-quote{left:100px;top:278px;font-size:21px;font-weight:600}
.hero-copy{left:100px;top:325px;width:390px;font-size:13.5px;line-height:25px;color:#333}
.hero-copy b{color:var(--teal);font-weight:600}
.field-label{left:100px;top:423px;font-size:13px;color:#333}
.hero-input{left:100px;top:451px;width:349px;height:50px;border:2px solid var(--green);border-radius:3px;padding:0 14px;display:flex;align-items:center;font-size:13px;color:#444}
.btn-green{background:var(--green);color:#fff;font-weight:700;border-radius:3px;display:flex;align-items:center;justify-content:center}
.hero-btn{left:100px;top:509px;width:153px;height:51px;font-size:15px}
.review-badge{left:100px;top:658px;width:88px;height:36px;border-radius:4px;background:#eef1f5}
.ph{position:absolute}
/* section headings */
.sec-head{position:absolute;font-size:27px;font-weight:700}
.sec-head .hl{position:absolute;left:-22px;top:-22px;width:80px;height:72px;background:var(--pale-green);transform:skew(-8deg) rotate(-8deg);z-index:-1;border-radius:4px}
.sec-rule{position:absolute;height:3px;width:75px;background:var(--teal)}
/* cards */
.card{position:absolute;width:321px;height:507px;background:#fff;box-shadow:0 2px 10px rgba(0,0,0,.08)}
.card .date{position:absolute;left:20px;top:26px;font-size:12px;font-weight:700;color:var(--teal)}
.card .dots{position:absolute;right:22px;top:28px;width:4px;height:18px;background:radial-gradient(circle,#aaa 1.8px,transparent 2px) 0 0/4px 6px}
.card h3{position:absolute;left:20px;top:60px;font-size:21px;line-height:30px;font-weight:700;width:280px}
.card .pic{position:absolute;left:20px;top:138px;width:281px;height:152px;border-radius:40px 40px 18px 18px}
.card .specs{position:absolute;left:0;top:305px;width:321px;height:52px;background:var(--spec);display:flex;padding:8px 20px 0;font-size:11px}
.card .specs div{line-height:18px;color:#222;font-weight:600}
.card .specs span{display:block;color:var(--teal);font-weight:700}
.card .price{position:absolute;left:16px;top:383px;font-size:27px;font-weight:700;color:var(--teal)}
.card .price sup{font-size:13px;vertical-align:12px}
.card .avail{position:absolute;right:18px;top:382px;width:107px;height:42px;font-size:13px}
.card .more{position:absolute;left:20px;top:446px;width:282px;height:42px;border:2px solid var(--teal);border-radius:4px;color:var(--teal);font-size:14px;font-weight:700;display:flex;align-items:center;justify-content:center}
/* sell */
.sell{left:117px;top:2112px;width:966px;height:358px;background:#fff;box-shadow:0 3px 16px rgba(0,0,0,.08)}
.sell .eyebrow{position:absolute;left:20px;top:25px;font-size:12px;font-weight:700;color:var(--teal)}
.sell h2{position:absolute;left:20px;top:52px;font-size:24px;line-height:31px;font-weight:700;width:380px}
.sell h2 em{font-style:normal;color:var(--green)}
.sell .sub{position:absolute;left:20px;top:135px;font-size:14px;color:#555}
.sell .see{position:absolute;left:20px;top:170px;font-size:11.5px;color:#222}
.sell .see b{color:var(--teal);font-weight:400}
.sell .lab{position:absolute;top:216px;font-size:11px;color:#888}
.sell .inp{position:absolute;top:238px;width:251px;height:38px;border:1px solid #ddd;background:#fafafa;font-size:11px;padding:0 14px;display:flex;align-items:center;color:#444}
.sell .b1{position:absolute;left:20px;top:294px;width:251px;height:38px;font-size:12px}
.sell .b2{position:absolute;left:287px;top:294px;width:251px;height:38px;border:2px solid var(--green);color:var(--green);font-size:12px;font-weight:700;display:flex;align-items:center;justify-content:center}
.sell .photo{position:absolute;left:566px;top:0;width:400px;height:358px;border-radius:0 12px 12px 0;background:linear-gradient(135deg,#8ba0b8,#5f7a50 70%,#7a9a4a)}
/* welcome */
.welcome-photo{left:0;top:2597px;width:605px;height:523px;background:linear-gradient(120deg,#c9cdd3,#e8e4de 55%,#b7bcc4)}
.welcome-panel{left:605px;top:2597px;width:595px;height:523px;background:var(--teal);color:#fff;padding:96px 95px 0 26px}
.welcome-panel h2{font-size:33px;font-weight:700;margin-bottom:22px;white-space:nowrap}
.welcome-panel p{font-size:12px;line-height:24px;text-align:justify;color:#eaf8f5}
.welcome-panel .btn-green{width:125px;height:42px;margin-top:24px;font-size:14px}
/* testimonials */
.quote-card{position:absolute;width:392px;height:152px;background:#fff;box-shadow:0 2px 12px rgba(0,0,0,.07)}
.avatar{position:absolute;width:84px;height:84px;border-radius:50%;border:4px solid #fff;box-shadow:0 2px 8px rgba(0,0,0,.12)}
.qmark{position:absolute;left:62px;top:18px;color:var(--green);font-size:44px;font-weight:800;line-height:1}
.qtext{position:absolute;left:97px;top:20px;width:270px;font-size:12px;line-height:20.5px;color:#555}
.qname{position:absolute;left:107px;top:98px;font-size:12.5px;font-weight:700}
.qrule{position:absolute;left:107px;top:118px;width:36px;height:2px;background:var(--teal)}
.qfrom{position:absolute;left:107px;top:125px;font-size:10.5px;color:#666}
/* footer */
.foot-about{left:100px;top:4150px;width:335px;font-size:12px;line-height:20px;color:#555}
.foot-btn{left:100px;top:4246px;width:127px;height:42px;font-size:14px}
.foot-col{position:absolute;top:4068px}
.foot-col h4{font-size:14px;font-weight:700;margin-bottom:8px}
.foot-col .r{width:35px;height:2px;background:var(--teal);margin-bottom:16px}
.foot-col a{display:block;font-size:12px;color:#666;text-decoration:none;line-height:30px}
.foot-col p{font-size:12px;color:#555;line-height:19px}
.foot-line{left:100px;top:4326px;width:1000px;height:1px;background:#ddd}
.copy{left:0;top:4347px;width:1200px;text-align:center;font-size:12px;color:#666}
</style>
</head>
<body>

<svg class="shapes" viewBox="0 0 1200 4383" aria-hidden="true">
  <polygon points="476,196 561,250 520,391 455,320" fill="var(--pale-green)"/>
  <polygon points="1200,650 1020,650 1060,775 1130,775" fill="var(--pale-green)"/>
  <path d="M442,0 H1200 V694 H760 Q700,694 690,640 L612,330 Z" fill="var(--teal)"/>
  <polygon points="0,960 1200,905 1200,1960 0,1990" fill="var(--soft)"/>
  <polygon points="0,1990 1200,1960 1200,2010 0,2010" fill="#fff"/>
  <polygon points="0,2597 900,2597 1200,2585 1200,2620 0,2620" fill="var(--pale-green)"/>
  <polygon points="0,3105 1200,3105 0,3150" fill="var(--pale-green)"/>
  <polygon points="0,3918 1200,3918 1200,4383 0,4383" fill="var(--soft)"/>
  <polygon points="1200,3918 1200,4005 880,4015" fill="var(--pale-green)"/>
  <line x1="647" y1="178" x2="1079" y2="178" stroke="var(--green)" stroke-width="3" stroke-dasharray="8 5"/>
  <line x1="647" y1="178" x2="783" y2="178" stroke="var(--green)" stroke-width="3"/>
</svg>

<!-- header -->
<div class="brand" style="left:100px;top:30px">
  <div class="brand-name">TideWillowNook.com</div>
  <div class="brand-dot"></div>
</div>
<div class="abs phone-box">
  <svg width="18" height="18" viewBox="0 0 24 24" fill="none" stroke="#fff" stroke-width="2"><path d="M5 3h4l2 5-3 2a11 11 0 0 0 6 6l2-3 5 2v4a2 2 0 0 1-2 2A17 17 0 0 1 3 5a2 2 0 0 1 2-2z"/></svg>
</div>
<div class="abs phone-text">555-014-2290</div>
<div class="abs menu">Menu
  <svg width="20" height="12" viewBox="0 0 20 12" stroke="#fff" stroke-width="1.6"><line x1="0" y1="1" x2="20" y2="1"/><line x1="4" y1="6" x2="20" y2="6"/><line x1="0" y1="11" x2="20" y2="11"/></svg>
</div>
<div class="abs login">
  <svg width="12" height="13" viewBox="0 0 12 13" fill="none" stroke="#fff" stroke-width="1.3"><circle cx="6" cy="4" r="3"/><path d="M1 12c0-3 2-4.5 5-4.5s5 1.5 5 4.5"/></svg>Login
</div>

<div class="abs advertise">ADVERTISE YOUR CAR 100% FREE</div>
<div class="step" style="left:619px">01</div>
<div class="step" style="left:769px">02</div>
<div class="step" style="left:915px">03</div>
<div class="step" style="left:1065px">04</div>
<div class="step-cap" style="left:576px;width:84px;text-align:center">Create your<br>FREE Advert</div>
<div class="step-cap" style="left:700px;width:110px;text-align:center">Review Offers<br>from rated buyers</div>
<div class="step-cap" style="left:845px;width:100px;text-align:right">Agree the deal<br>with your chosen<br>buyer</div>
<div class="step-cap" style="left:980px;width:118px;text-align:right">When You're<br>totally happy,<br>exchagen contact<br>information and<br>arrange collection<br>or delivery</div>

<!-- hero -->
<h1 class="abs hero-title">Get Your Free In Person Cash Offer Today</h1>
<div class="abs hero-quote">“Don't Sell Til You Give Me A Yell”</div>
<p class="abs hero-copy"><b>Fast</b> – I'll Be at Your Door Today, <b>Fair</b> – Get Fair Price for Your Vehicle, <b>Friendly</b> – Trusted for Over 25 Years, Hassle <b>Free</b> – I Handle All the Paperwork</p>
<div class="abs field-label">Enter your registration</div>
<div class="abs hero-input">e.g ASTDEDE</div>
<div class="abs btn-green hero-btn">Schedule Now</div>
<div class="abs review-badge" role="img" aria-label="Review rating badge"></div>
<div class="ph" style="left:470px;top:228px;width:500px;height:420px;border-radius:120px 120px 60px 60px;background:radial-gradient(ellipse at 55% 70%,#e9ecef,#c2c8cf 55%,rgba(51,184,164,0) 75%)" role="img" aria-label="Two smiling women standing behind a white SUV"></div>

<!-- deals -->
<h2 class="sec-head" style="left:122px;top:838px"><span class="hl"></span>Latest our car deals</h2>
<div class="sec-rule" style="left:297px;top:882px"></div>

<div class="card" style="left:100px;top:948px">
  <div class="date">Sunday,Oct 21,2020</div><div class="dots"></div>
  <h3>Kestrel Pico '1'1.0<br>66BHP 5 SPEED 5dr</h3>
  <div class="pic" role="img" aria-label="Blue hatchback car" style="background:linear-gradient(180deg,#fff 10%,#3a5fb0 45%,#1f3773 80%,#fff 95%)"></div>
  <div class="specs"><div style="width:78px"><span>POWER</span>250 KW</div><div style="width:99px"><span>0-100KM/H</span>6.4 Second</div><div><span>MAX SPEED</span>160KM/H</div></div>
  <div class="price"><sup>$</sup>7,650</div><div class="btn-green avail">AVAILABLE</div>
  <div class="more">Read more</div>
</div>
<div class="card" style="left:439px;top:948px">
  <div class="date">Sunday,Oct 21,2020</div><div class="dots"></div>
  <h3>Kestrel Pico '1'1.0<br>66BHP 5 SPEED 5dr</h3>
  <div class="pic" role="img" aria-label="Red hatchback car" style="background:linear-gradient(180deg,#fff 10%,#d42a30 45%,#8a1218 80%,#fff 95%)"></div>
  <div class="specs"><div style="width:78px"><span>POWER</span>250 KW</div><div style="width:99px"><span>0-100KM/H</span>6.4 Second</div><div><span>MAX SPEED</span>160KM/H</div></div>
  <div class="price"><sup>$</sup>11,650</div><div class="btn-green avail">AVAILABLE</div>
  <div class="more">Read more</div>
</div>
<div class="card" style="left:778px;top:948px">
  <div class="date">Sunday,Oct 21,2020</div><div class="dots"></div>
  <h3>Kestrel Pico '1'1.0<br>66BHP 5 SPEED 5dr</h3>
  <div class="pic" role="img" aria-label="Dark grey compact MPV" style="background:linear-gradient(180deg,#fff 10%,#4a4d52 45%,#26282b 80%,#fff 95%)"></div>
  <div class="specs"><div style="width:78px"><span>POWER</span>250 KW</div><div style="width:99px"><span>0-100KM/H</span>6.4 Second</div><div><span>MAX SPEED</span>160KM/H</div></div>
  <div class="price"><sup>$</sup>8,650</div><div class="btn-green avail">AVAILABLE</div>
  <div class="more">Read more</div>
</div>
<div class="card" style="left:100px;top:1476px">
  <div class="date">Sunday,Oct 21,2020</div><div class="dots"></div>
  <h3>Kestrel Pico '1'1.0<br>66BHP 5 SPEED 5dr</h3>
  <div class="pic" role="img" aria-label="White motorhome RV" style="background:linear-gradient(180deg,#fff 5%,#e3e5e8 35%,#a9adb3 80%,#fff 95%)"></div>
  <div class="specs"><div style="width:78px"><span>POWER</span>250 KW</div><div style="width:99px"><span>0-100KM/H</span>6.4 Second</div><div><span>MAX SPEED</span>160KM/H</div></div>
  <div class="price"><sup>$</sup>7,650</div><div class="btn-green avail">AVAILABLE</div>
  <div class="more">Read more</div>
</div>
<div class="card" style="left:439px;top:1476px">
  <div class="date">Sunday,Oct 21,2020</div><div class="dots"></div>
  <h3>Kestrel Pico '1'1.0<br>66BHP 5 SPEED 5dr</h3>
  <div class="pic" role="img" aria-label="White motor yacht" style="background:linear-gradient(180deg,#fff 10%,#d6dde6 45%,#8796a8 75%,#fff 95%)"></div>
  <div class="specs"><div style="width:78px"><span>POWER</span>250 KW</div><div style="width:99px"><span>0-100KM/H</span>6.4 Second</div><div><span>MAX SPEED</span>160KM/H</div></div>
  <div class="price"><sup>$</sup>11,650</div><div class="btn-green avail">AVAILABLE</div>
  <div class="more">Read more</div>
</div>
<div class="card" style="left:778px;top:1476px">
  <div class="date">Sunday,Oct 21,2020</div><div class="dots"></div>
  <h3>Kestrel Pico '1'1.0<br>66BHP 5 SPEED 5dr</h3>
  <div class="pic" role="img" aria-label="Dark grey compact MPV" style="background:linear-gradient(180deg,#fff 10%,#4a4d52 45%,#26282b 80%,#fff 95%)"></div>
  <div class="specs"><div style="width:78px"><span>POWER</span>250 KW</div><div style="width:99px"><span>0-100KM/H</span>6.4 Second</div><div><span>MAX SPEED</span>160KM/H</div></div>
  <div class="price"><sup>$</sup>8,650</div><div class="btn-green avail">AVAILABLE</div>
  <div class="more">Read more</div>
</div>

<!-- sell my car -->
<section class="abs sell">
  <div class="eyebrow">Sell My Car</div>
  <h2>Make $1,254 more by selling your car with <em>Tide Willow Nook</em></h2>
  <div class="sub">Get the price you deserve</div>
  <div class="see">See our <b>advertising price</b></div>
  <div class="lab" style="left:20px">Registration</div>
  <div class="lab" style="left:287px">Current Mileage</div>
  <div class="inp" style="left:20px">e.g LL 58 JFK</div>
  <div class="inp" style="left:287px">e.g 50,000</div>
  <div class="btn-green b1">Create Your Advert</div>
  <div class="b2">Manage existing adverts</div>
  <div class="photo" role="img" aria-label="Family sitting in the open boot of a car on grass"></div>
</section>

<!-- welcome -->
<div class="abs welcome-photo" role="img" aria-label="Dealer handing car keys and cash to a smiling woman"></div>
<section class="abs welcome-panel">
  <h2>Welcome to Tide Willow Nook</h2>
  <p>Lorem ipsum dolor sit amet, consectetur adipiscing elit, sed do eiusmod tempor incididunt ut labore et dolore magna aliqua. Quis ipsum suspendisse ultrices gravida. Risus commodo viverra maecenas accumsan lacus vel facilisis. Lorem ipsum dolor sit amet, consectetur adipiscing elit, sed do eiusmod tempor incididunt ut labore et dolore magna aliqua. Quis ipsum suspendisse ultrices gravida. Risus commodo viverra maecenas accumsan lacus vel facilisis. Lorem ipsum dolor sit amet, consectetur adipiscing elit, sed do eiusmod tempor incididunt ut labore et dolore magna aliqua. Quis ipsum suspendisse ultrices gravida.</p>
  <div class="btn-green">Learn more</div>
</section>

<!-- testimonials -->
<h2 class="sec-head" style="left:122px;top:3290px"><span class="hl"></span>What our customers say</h2>
<div class="sec-rule" style="left:357px;top:3334px"></div>

<div class="quote-card" style="left:183px;top:3422px">
  <div class="qmark">“</div>
  <p class="qtext">Lorem ipsum dolor sit amr adipiscing elit, sed do eiusmod tempor incididun labore et dolore magna aliqua. Quis ipsum suspendis</p>
  <div class="qname">Marcus Hale</div><div class="qrule"></div><div class="qfrom">From USA</div>
</div>
<div class="avatar" style="left:145px;top:3456px;background:linear-gradient(#d9dde2,#3d3f45)" role="img" aria-label="Customer portrait"></div>
<div class="quote-card" style="left:664px;top:3422px">
  <div class="qmark">“</div>
  <p class="qtext">Lorem ipsum dolor sit amr adipiscing elit, sed do eiusmod tempor incididun labore et dolore magna aliqua. Quis ipsum suspendis</p>
  <div class="qname">Marcus Hale</div><div class="qrule"></div><div class="qfrom">From USA</div>
</div>
<div class="avatar" style="left:626px;top:3456px;background:linear-gradient(#e9e3dc,#a47b5e)" role="img" aria-label="Customer portrait"></div>
<div class="quote-card" style="left:183px;top:3634px">
  <div class="qmark">“</div>
  <p class="qtext">Lorem ipsum dolor sit amr adipiscing elit, sed do eiusmod tempor incididun labore et dolore magna aliqua. Quis ipsum suspendis</p>
  <div class="qname">Marcus Hale</div><div class="qrule"></div><div class="qfrom">From USA</div>
</div>
<div class="avatar" style="left:145px;top:3668px;background:linear-gradient(#e7ebef,#7c8fa8)" role="img" aria-label="Customer portrait"></div>
<div class="quote-card" style="left:664px;top:3634px">
  <div class="qmark">“</div>
  <p class="qtext">Lorem ipsum dolor sit amr adipiscing elit, sed do eiusmod tempor incididun labore et dolore magna aliqua. Quis ipsum suspendis</p>
  <div class="qname">Marcus Hale</div><div class="qrule"></div><div class="qfrom">From USA</div>
</div>
<div class="avatar" style="left:626px;top:3668px;background:linear-gradient(#cfd3d8,#5a5550)" role="img" aria-label="Customer portrait"></div>

<!-- footer -->
<div class="brand" style="left:100px;top:4082px">
  <div class="brand-name" style="font-size:19px">TideWillowNook.com</div>
  <div class="brand-dot"></div>
</div>
<p class="abs foot-about">We offer the most convenient way of selling your vehicle. We will come to you at a place of your choosing, i.e. home, office, or any other public place. We will give you an in person cash offer on the spot.</p>
<div class="abs btn-green foot-btn">Ask Question</div>

<div class="foot-col" style="left:511px"><h4>Quick Links</h4><div class="r"></div><a>Home</a><a>About Us</a><a>Term And Condition</a><a>Contact Us</a></div>
<div class="foot-col" style="left:708px"><h4>Connect With US</h4><div class="r"></div><a>Community</a><a>Videos</a><a>Gallery</a><a>Boards</a></div>
<div class="foot-col" style="left:921px;width:180px"><h4>Contact Us</h4><div class="r"></div>
  <p>Feel free get in touch with us via phone or send us a message</p>
  <p style="margin-top:14px;color:var(--ink);font-weight:700">555-014-2290<br>info@tidewillownook.com</p>
</div>
<div class="abs foot-line"></div>
<div class="abs copy">TideWillowNook Copyright © All right reserved</div>

</body>
</html>
```